Visitenkarten-Design für K17.eu - TradeWing Finanz
Zielgruppe
Smartphone-Banking mit Mehrwert
Aufgabenstellung
Bitte entwerfen Sie kreative Visitenkarten für uns.
- Halten Sie einen Platz/Rahmen frei für Fotos, die wir nachträglich einsetzen, und kennzeichnen diesen.
- Halten Sie einen Patz/Rahmen für Vor- und Nachname sowie für die Berufsbezeichnung frei und kennzeichnen diesen.
- Halten Sie einen Platz/Rahmen für die Telefonnummern und die Email-Adressen frei und kennzeichnen diesen.
Alle Visitenkarten sollen folgende Daten beinhalten:
Vorname Nachname*
Berufsbezeichnung*
Mobile:
Office:
Email:
Domain:
* = individuell, jeder Mitarbeiter hat eigene Daten
Die Farben müssen sich an unserem CI-Design orientieren, orange/weiß/schwarz/grau -
Außerdem finden Sie unser Logo in der Anlage, welches Sie bitte auf der Karte platzieren.
Bitte liefern Sie uns die Designs in verschiedenen Formaten - psd, ai, eps, jpg, png
Bei Fragen zögern Sie nicht, uns zu kontaktieren. Danke.

```html
<!DOCTYPE html>
<html lang="de">
<head>
<meta charset="utf-8">
<title>K17 Visitenkarte</title>
<link href="https://fonts.googleapis.com/css2?family=Arimo:wght@400;700&display=swap" rel="stylesheet">
<style>
  :root {
    --orange: #d47a37;
    --grey: #5f5f5f;
    --text: #4a4a4a;
    --white: #ffffff;
    --backdrop: #dcdcdc;
  }
  * { margin: 0; padding: 0; box-sizing: border-box; }
  html, body { width: 1106px; height: 1200px; overflow: hidden; }
  body {
    background: var(--backdrop);
    font-family: "Arimo", Arial, sans-serif;
    position: relative;
  }
  .card {
    position: absolute;
    top: 278px;
    width: 420px;
    height: 644px;
    box-shadow: 0 6px 18px rgba(0,0,0,0.12);
  }
  .card-front { left: 103px; background: var(--white); }
  .card-back { left: 583px; background: var(--orange); }

  .brand {
    position: absolute;
    display: flex;
    flex-direction: column;
    align-items: flex-start;
  }
  .brand-row { display: flex; align-items: center; gap: 10px; }
  .brand-square { display: block; background: var(--grey); }
  .brand-name { font-weight: 700; line-height: 1; }
  .brand-domain { font-weight: 700; color: var(--grey); line-height: 1; }

  .card-front .brand { left: 124px; top: 30px; }
  .card-front .brand-square { width: 30px; height: 30px; }
  .card-front .brand-name { font-size: 50px; color: var(--orange); }
  .card-front .brand-domain { font-size: 22px; margin-top: 10px; margin-left: 22px; }

  .company-address {
    position: absolute;
    top: 166px; left: 0; width: 100%;
    text-align: center;
    font-size: 19px;
    line-height: 24px;
    color: var(--text);
    font-style: normal;
  }
  .company-address strong { font-weight: 700; }

  .portrait {
    position: absolute;
    left: 285px; top: 393px;
    width: 110px; height: 109px;
    background: linear-gradient(135deg, #e9e6e4 0%, #b48a6a 45%, #3a2f2b 100%);
  }

  .person { position: absolute; left: 27px; top: 427px; }
  .person-name { font-size: 22px; color: var(--orange); line-height: 28px; }
  .person-role { font-size: 19px; color: var(--text); line-height: 26px; }

  .contact {
    position: absolute; left: 27px; top: 512px;
    list-style: none;
  }
  .contact li {
    font-size: 18px; color: var(--text);
    line-height: 29px; padding-left: 50px;
    position: relative;
  }
  .contact svg { position: absolute; left: 0; }
  .icon-phone { top: 2px; }
  .icon-mail { top: 4px; }

  .accent-band {
    position: absolute; left: 0; bottom: 0;
    width: 100%; height: 31px;
    background: var(--orange);
  }

  .card-back .brand { left: 79px; top: 404px; }
  .card-back .brand-square { width: 42px; height: 42px; }
  .card-back .brand-name { font-size: 86px; color: var(--white); }
  .card-back .brand-domain { font-size: 30px; margin-top: 14px; margin-left: 30px; }
</style>
</head>
<body>
  <section class="card card-front">
    <div class="brand">
      <div class="brand-row">
        <span class="brand-square"></span>
        <span class="brand-name">K17</span>
      </div>
      <span class="brand-domain">www.k17.eu</span>
    </div>

    <address class="company-address">
      <strong>K17 GmbH</strong><br>
      Lindenweg 9<br>
      84028 Landshut<br>
      Germany
    </address>

    <div class="portrait" role="img" aria-label="Platz für Mitarbeiterfoto"></div>

    <div class="person">
      <p class="person-name">Vorname Nachname</p>
      <p class="person-role">Berufsbezeichnung</p>
    </div>

    <ul class="contact">
      <li>
        <svg class="icon-phone" width="30" height="46" viewBox="0 0 30 46" fill="none" stroke="#d47a37" stroke-width="2">
          <rect x="2" y="1" width="26" height="44" rx="3"/>
          <line x1="2" y1="7" x2="28" y2="7"/>
          <line x1="2" y1="38" x2="28" y2="38"/>
          <line x1="12" y1="4" x2="18" y2="4"/>
        </svg>
        +49 160 xxxxxxx
      </li>
      <li>+49 871 xxxxxx-xx</li>
      <li>
        <svg class="icon-mail" width="30" height="20" viewBox="0 0 30 20" fill="none" stroke="#d47a37" stroke-width="2">
          <rect x="1" y="1" width="28" height="18"/>
          <polyline points="1,1 15,12 29,1"/>
          <line x1="1" y1="19" x2="11" y2="9"/>
          <line x1="29" y1="19" x2="19" y2="9"/>
        </svg>
        vorname@k17.eu
      </li>
    </ul>

    <div class="accent-band"></div>
  </section>

  <section class="card card-back">
    <div class="brand">
      <div class="brand-row">
        <span class="brand-square"></span>
        <span class="brand-name">K17</span>
      </div>
      <span class="brand-domain">www.k17.eu</span>
    </div>
  </section>
</body>
</html>
```